UX revamp for crypto platform mobile app

re-design the assets of a mobile app to give them a sleek, current and modern feel see reference below.
The current app has 3 main menus with subfunctions:
Wallet: Send - Receive - Top-up with shortcut to other main menus
Talents: User can support talent and see his support
Rewards: User can purchase rewards from Talents - Clubs - Plumtoken

Target Market(s)

Youth fans of sports and entertainment

Industry/Entity Type

Blockchain

Colors

Designer to choose colors to be used in the design.

Requirements
Must have
• Modern - sleek - stylish - current trends design
Nice to have
• Need to be clean design
Should not have
• too dark and heavy

```html
<!DOCTYPE html>
<html lang="en">
<head>
<meta charset="utf-8">
<title>Menu</title>
<link href="https://fonts.googleapis.com/css2?family=Montserrat:wght@400;500;600;700&family=Roboto:wght@400;500&display=swap" rel="stylesheet">
<style>
  :root {
    --black: #0b0b0b;
    --white: #ffffff;
    --wallet-light: #c7b9a9;
    --wallet-dark: #7f7165;
    --talents-light: #b49c7d;
    --talents-dark: #7a6349;
    --rewards-light: #e9b86a;
    --rewards-dark: #b47a3c;
    --pill-wallet: #c8b19b;
    --pill-talents: #6a5342;
    --pill-rewards: #1c8c8a;
  }
  * { margin: 0; padding: 0; box-sizing: border-box; }
  html, body { width: 752px; height: 1200px; overflow: hidden; }
  body { background: var(--black); font-family: "Montserrat", sans-serif; color: var(--white); }
  .screen { width: 752px; height: 1200px; display: flex; flex-direction: column; }

  .status-bar {
    height: 38px; background: var(--black); display: flex; align-items: center;
    justify-content: space-between; padding: 0 18px;
    font-family: "Roboto", sans-serif; font-size: 21px; color: #e8e8e8;
  }
  .status-left, .status-right { display: flex; align-items: center; gap: 10px; }
  .status-right svg { display: block; }

  .app-header {
    height: 82px; background: var(--black); position: relative;
    display: flex; align-items: center; justify-content: space-between; padding: 0 26px;
    z-index: 2;
  }
  .app-title { font-size: 42px; font-weight: 700; letter-spacing: 1px; }
  .header-pointer {
    position: absolute; left: 50%; bottom: -13px; transform: translateX(-50%);
    width: 0; height: 0; border-left: 14px solid transparent; border-right: 14px solid transparent;
    border-top: 14px solid var(--black);
  }

  .menu-list { flex: 1; display: flex; flex-direction: column; }
  .menu-card {
    flex: 1; position: relative; display: flex; flex-direction: column;
    align-items: center; justify-content: center; text-align: center; padding-top: 40px;
    border-bottom: 2px solid rgba(255,255,255,0.35);
  }
  .menu-card:last-child { border-bottom: none; }
  .card-photo { position: absolute; inset: 0; }
  .wallet .card-photo { background: linear-gradient(135deg, var(--wallet-light) 0%, #a89888 45%, var(--wallet-dark) 100%); }
  .talents .card-photo { background: linear-gradient(160deg, var(--talents-light) 0%, #957c5f 50%, var(--talents-dark) 100%); }
  .rewards .card-photo { background: linear-gradient(150deg, var(--rewards-light) 0%, #d39a52 50%, var(--rewards-dark) 100%); }

  .card-icon {
    position: absolute; left: 24px; top: 26px; width: 40px; height: 40px; border-radius: 50%;
    background: var(--white); color: #333; font-size: 9px; font-weight: 600;
    display: flex; align-items: center; justify-content: center;
  }
  .card-tag {
    position: absolute; right: 24px; top: 26px; padding: 8px 22px; border-radius: 20px;
    font-size: 18px; font-weight: 600; letter-spacing: 0.5px; color: var(--white);
  }
  .wallet .card-tag { background: var(--pill-wallet); }
  .talents .card-tag { background: var(--pill-talents); }
  .rewards .card-tag { background: var(--pill-rewards); }

  .card-title {
    position: relative; font-size: 84px; font-weight: 500; letter-spacing: 2px; line-height: 1;
    text-shadow: 0 2px 8px rgba(0,0,0,0.25);
  }
  .card-text {
    position: relative; margin-top: 14px; font-size: 21px; font-weight: 400; line-height: 1.3;
    letter-spacing: 0.5px; text-transform: uppercase; text-shadow: 0 1px 4px rgba(0,0,0,0.3);
  }
  .card-text strong { font-weight: 700; }
</style>
</head>
<body>
<main class="screen">
  <div class="status-bar">
    <div class="status-left">
      <svg width="22" height="20" viewBox="0 0 22 20"><rect x="1" y="1" width="20" height="18" rx="2" fill="none" stroke="#e8e8e8" stroke-width="2"/><rect x="6" y="6" width="10" height="8" fill="#e8e8e8"/></svg>
      <svg width="22" height="20" viewBox="0 0 22 20"><rect x="1" y="1" width="20" height="18" rx="2" fill="none" stroke="#e8e8e8" stroke-width="2"/><path d="M4 15 L9 9 L13 13 L16 10 L19 15 Z" fill="#e8e8e8"/></svg>
    </div>
    <div class="status-right">
      <svg width="22" height="20" viewBox="0 0 22 20"><path d="M2 6 h8 v8 h-8 z M10 6 l8 -4 v16 l-8 -4" fill="none" stroke="#e8e8e8" stroke-width="2"/></svg>
      <svg width="24" height="20" viewBox="0 0 24 20"><path d="M12 18 L1 6 A16 16 0 0 1 23 6 Z" fill="#e8e8e8"/></svg>
      <svg width="20" height="20" viewBox="0 0 20 20"><path d="M2 18 L18 2 V18 Z" fill="#e8e8e8"/></svg>
      <span>64%</span>
      <svg width="12" height="22" viewBox="0 0 12 22"><rect x="1" y="3" width="10" height="18" rx="1" fill="none" stroke="#e8e8e8" stroke-width="2"/><rect x="4" y="0" width="4" height="3" fill="#e8e8e8"/><rect x="3" y="9" width="6" height="10" fill="#e8e8e8"/></svg>
      <span>15:17</span>
    </div>
  </div>

  <header class="app-header">
    <svg class="menu-button" width="40" height="32" viewBox="0 0 40 32" aria-label="Open list">
      <g fill="#fff">
        <rect x="0" y="2" width="8" height="7"/><rect x="12" y="2" width="28" height="7"/>
        <rect x="0" y="13" width="8" height="7"/><rect x="12" y="13" width="28" height="7"/>
        <rect x="0" y="24" width="8" height="7"/><rect x="12" y="24" width="28" height="7"/>
      </g>
    </svg>
    <h1 class="app-title">MENU</h1>
    <svg class="search-button" width="38" height="38" viewBox="0 0 38 38" aria-label="Search">
      <circle cx="15" cy="15" r="11" fill="none" stroke="#fff" stroke-width="4"/>
      <line x1="23" y1="23" x2="35" y2="35" stroke="#fff" stroke-width="5" stroke-linecap="round"/>
    </svg>
    <span class="header-pointer"></span>
  </header>

  <section class="menu-list">
    <article class="menu-card wallet">
      <div class="card-photo" role="img" aria-label="Photo of hands holding a smartphone, in warm muted tones"></div>
      <span class="card-icon">ICON</span>
      <span class="card-tag">LOREMIPS</span>
      <h2 class="card-title">WALLET</h2>
      <p class="card-text"><strong>Send</strong> - <strong>Receive</strong> - <strong>Top-up</strong> with<br>shortcut to other <strong>main menus</strong></p>
    </article>

    <article class="menu-card talents">
      <div class="card-photo" role="img" aria-label="Photo of a compass dial pointing to the word talent, in brown tones"></div>
      <span class="card-icon">ICON</span>
      <span class="card-tag">LOREMIPS</span>
      <h2 class="card-title">TALENTS</h2>
      <p class="card-text">User can <strong>support talent</strong><br>and see his <strong>support</strong></p>
    </article>

    <article class="menu-card rewards">
      <div class="card-photo" role="img" aria-label="Photo of happy shoppers with shopping bags, in golden orange tones"></div>
      <span class="card-icon">ICON</span>
      <span class="card-tag">LOREMIPS</span>
      <h2 class="card-title">REWARDS</h2>
      <p class="card-text">User can <strong>purchase rewards</strong><br>from <strong>Talents</strong> - <strong>Clubs</strong> - <strong>Plumtoken</strong></p>
    </article>
  </section>
</main>
</body>
</html>
```